QT482 - Guard, Track, Tune, Steer - OT Cyber Security Software, KPI Visualisation Software and

Build Website - we require a website with approx 5 tabs on scrolling pane screen - Home, Who We are, Cyber Security, Visualisation, Trusted Partners, Support, Contact, single scrolling panel or tab click to page with images and 2-3 paragraphs of text - wording and links to partners will be provided along with company logo

Target Market(s)

Process Control Markets - Oil and Gas clients, Telecommunications Operators, IOT companies, manufacturing, transport sector etc

Industry/Entity Type

Security

Coding

Coded - Design and coding required

Number of Pages Required

5+ page

Font styles to use
Sans Serif

Colors
0255a3
3176b5
85abd2
f04a50
ec1f27
1b1b1b
474747
919191
d3d3d3

Requirements
Must have
• Scrolling pane / page with tabs along the top -
• Who We are - software and professional services provider for Process Control Cyber Security and Data visualisation
• Guard Track Tune Steer -
• define and defend process control networks, measure, manage, visualise data sets from any source etc
• Process Control Cyber Security - images and wording - area for wording can be created and left to be fully populated etc
• Visualisation - data set visualisation from desk top / tablet / mobile device,
• Trusted Partners - links to www.brevanix.example www.lumicore.example www.dorvale.example.au
• Support
• Contact Details
• images for cyber security risks etc
• data visualisation / visual KPI - software package
• Support - link to www.dorvale.example.au for NOC and Customer Support - sections for Gold, Silver and Bronze support package - we will add wording later
Nice to have
• Colours - blues / blacks / grey - cyber security information and sections,
• reds etc for visualisation sections
• Use similar colours as logo for rest of pages

```html
<!DOCTYPE html>
<html lang="en">
<head>
<meta charset="utf-8">
<title>QT482 – OT Cyber Security &amp; KPI Visualisation</title>
<link rel="stylesheet" href="https://fonts.googleapis.com/css2?family=Ropa+Sans&family=Poppins:wght@300;400;500&display=swap">
<style>
:root{
  --blue:#0255a3;
  --blue-mid:#3176b5;
  --blue-light:#85abd2;
  --red:#f04a50;
  --red-deep:#ec1f27;
  --ink:#1b1b1b;
  --text:#474747;
  --grey:#919191;
  --line:#d3d3d3;
  --white:#ffffff;
}
*{margin:0;padding:0;box-sizing:border-box}
html,body{width:1200px;height:2956px;overflow:hidden;background:var(--white)}
body{font-family:"Poppins",sans-serif;color:var(--text);position:relative}
h1,h2,h3,.nav a,.btn{font-family:"Ropa Sans",sans-serif;font-weight:400}
.section{position:absolute;left:0;width:1200px}
.section-rule{position:absolute;left:573px;display:block;width:54px;height:3px}
.rule-red{background:var(--red)}
.rule-blue{background:var(--blue-mid)}
.rule-dark{background:var(--ink)}

/* header */
.site-header{top:0;height:143px;border-top:4px solid var(--blue);background:var(--white)}
.brand{position:absolute;left:540px;top:8px;width:120px;height:76px;display:flex;align-items:center;justify-content:center;gap:8px}
.brand-mark{width:12px;height:12px;border-radius:50%;background:var(--red-deep)}
.brand-name{font-family:"Ropa Sans",sans-serif;font-size:28px;color:var(--blue)}
.nav{position:absolute;top:96px;left:0;width:1200px;height:36px}
.nav a{position:absolute;top:0;height:36px;line-height:36px;font-size:16px;color:var(--ink);text-decoration:none;padding:0 14px}
.nav a.active{background:var(--blue);color:var(--white)}

/* hero */
.hero{top:143px;height:509px;background:linear-gradient(100deg,#3a3d42 0%,#6b6e72 45%,#8c8d8f 62%,#2b2c2f 100%)}
.hero h1{position:absolute;top:190px;width:100%;text-align:center;color:var(--white);font-size:37px;line-height:57px;letter-spacing:.5px}

/* who we are */
.about{top:652px;height:615px;background:var(--white)}
.about h2{position:absolute;top:52px;width:100%;text-align:center;font-size:32px;color:var(--ink)}
.about .section-rule{top:94px}
.lead{position:absolute;top:115px;width:100%;text-align:center;font-size:16px;color:var(--ink)}
.intro{position:absolute;top:153px;width:100%;text-align:center;font-size:12.5px;line-height:24px}
.cards{position:absolute;top:225px;left:86px;display:flex;gap:30px}
.card{width:234px;height:203px;border:1px solid var(--line);border-radius:3px;text-align:center;padding:22px 10px 0;box-shadow:0 1px 3px rgba(0,0,0,.05)}
.card h3{font-size:23px;color:var(--blue)}
.card-rule{display:block;width:22px;height:2px;margin:8px auto 12px;background:var(--blue)}
.card p{font-size:11.5px;line-height:22px;color:var(--ink)}
.card em{font-style:italic}
.principles{position:absolute;top:460px;width:100%;text-align:center;font-size:16px;color:var(--ink)}
.principles-text{position:absolute;top:494px;left:95px;width:1010px;text-align:center;font-size:12.5px;line-height:23px}

/* cyber */
.cyber{top:1267px;height:340px;background:radial-gradient(ellipse at 50% 70%,#26384f 0%,#131b27 55%,#0c0f15 100%)}
.cyber h2{position:absolute;top:80px;width:100%;text-align:center;color:var(--white);font-size:28px}
.cyber .section-rule{top:131px}
.cyber p{position:absolute;left:130px;width:940px;text-align:center;color:var(--white);font-size:13.5px;line-height:26px}

/* kpi */
.kpi{top:1607px;height:333px;display:flex}
.kpi-text{width:680px;height:333px;background:var(--red);color:var(--white);padding:66px 40px 0 85px}
.kpi-text h2{font-size:24px}
.kpi-text p{font-size:13.5px;line-height:26px;margin-top:22px}
.kpi-text p+p{margin-top:18px}
.kpi-image{width:520px;height:333px;background:linear-gradient(160deg,#0a1726 0%,#1c5a7d 50%,#0c2236 100%)}

/* partners */
.partners{top:1940px;height:273px;background:var(--white)}
.partners h2{position:absolute;top:52px;width:100%;text-align:center;font-size:28px;color:var(--ink)}
.partners .section-rule{top:93px}
.partner{position:absolute;top:135px;height:70px;display:flex;align-items:center;gap:10px;font-family:"Ropa Sans",sans-serif;font-size:30px;color:var(--ink);text-decoration:none}
.partner-mark{width:26px;height:26px;background:var(--ink)}

/* support */
.support{top:2213px;height:362px;background:linear-gradient(100deg,#2e3033 0%,#4b4d50 50%,#1f2022 100%)}
.support h2{position:absolute;top:70px;width:100%;text-align:center;color:var(--white);font-size:30px}
.support .section-rule{top:114px}
.support p{position:absolute;top:145px;left:125px;width:950px;text-align:center;color:var(--white);font-size:13.5px;line-height:26px}
.btn{position:absolute;top:247px;left:535px;width:130px;height:42px;line-height:40px;border:1px solid var(--white);color:var(--white);font-size:17px;text-align:center;text-decoration:none}

/* contact */
.contact{top:2575px;height:318px;background:linear-gradient(180deg,#e9f1f6 0%,#f7f9fb 60%,#ffffff 100%)}
.contact h2{position:absolute;top:52px;width:100%;text-align:center;color:var(--blue-mid);font-size:30px}
.contact .section-rule{top:96px}
.detail{position:absolute;top:135px;display:flex;align-items:flex-start;gap:12px;font-size:15px;line-height:21px;color:var(--ink)}
.detail svg{flex:none}
.detail.phone{font-family:"Ropa Sans",sans-serif;font-size:20px}
.contact-cta{position:absolute;top:210px;width:100%;text-align:center;font-size:15px;line-height:28px;color:var(--ink)}

/* footer */
.site-footer{top:2893px;height:63px;background:var(--ink);color:var(--white)}
.copyright{position:absolute;left:84px;top:24px;font-size:12px}
.social{position:absolute;right:84px;top:21px;display:flex;gap:14px}
.social span{width:22px;height:22px;border-radius:3px;background:var(--red)}
</style>
</head>
<body>

<header class="section site-header">
  <div class="brand"><span class="brand-mark"></span><span class="brand-name">QT482</span></div>
  <nav class="nav">
    <a class="active" href="#home" style="left:148px;width:72px;text-align:center;padding:0">Home</a>
    <a href="#who" style="left:244px">Who We are</a>
    <a href="#cyber" style="left:386px">Cyber Security</a>
    <a href="#visual" style="left:540px">Visualisation</a>
    <a href="#partners" style="left:685px">Trusted Partners</a>
    <a href="#support" style="left:857px">Support</a>
    <a href="#contact" style="left:970px">Contact</a>
  </nav>
</header>

<section class="section hero" id="home" role="img" aria-label="Photo of a hand on a laptop overlaid with network connection icons">
  <h1>YOUR NETWORK<br>AND YOUR DATA IS YOUR BUSINESS</h1>
</section>

<section class="section about" id="who">
  <h2>Who We are</h2>
  <span class="section-rule rule-red"></span>
  <p class="lead">Data defines the health of your business and the state of your operations at any moment of any day.</p>
  <p class="intro">Defending that data, the network on which you move that data and understanding what that data is telling you is key to the success of every business.<br>QT482 enables you to do that – Guard, Track, Tune, Steer – 365 days a year.</p>
  <div class="cards">
    <article class="card"><h3>Guard</h3><span class="card-rule"></span><p>Baseline your OT communications<br>with passive capture of<br>your assets<br><em>know your topology with<br>confidence</em></p></article>
    <article class="card"><h3>Track</h3><span class="card-rule"></span><p>Be alerted to any change in your<br>baseline OT environment in<br>real-time<br><em>Pro-actively manage your<br>threats</em></p></article>
    <article class="card"><h3>Tune</h3><span class="card-rule"></span><p>Turn your data sources<br><em>into powerful Visual Management<br>Tools -trust your data to<br>inform you</em></p></article>
    <article class="card"><h3>Steer</h3><span class="card-rule"></span><p>Customise and present your<br>dashboard in minutes<br>Start managing,<br>your way, in minutes</p></article>
  </div>
  <p class="principles">These are the core principles that QT482 delivers for your Enterprise.</p>
  <p class="principles-text">QT482 understands that data and networks are voluable and vulnerable so our business-critical software defines your network, the hardware, the interfaces and the protocols it carries.<br>We understand the core of your network how it operates and then how you need to secure your network, devices and data.</p>
</section>

<section class="section cyber" id="cyber" role="img" aria-label="Dark blue background of a digital padlock and network lines">
  <h2>Process Control Cyber Security</h2>
  <span class="section-rule rule-blue"></span>
  <p style="top:155px">Sed ut perspiciatis unde omnis iste natus error sit voluptatem accusantium doloremque laudantium, totam rem aperiam, eaque ipsa quae ab illo inventore veritatis et quasi</p>
  <p style="top:220px">architecto beatae vitae dicta sunt explicabo. Nemo enim ipsam voluptatem quia voluptas sit aspernatur</p>
</section>

<section class="section kpi" id="visual">
  <div class="kpi-text">
    <h2>KPI Visualisation</h2>
    <p>Sed ut perspiciatis unde omnis iste natus error sit voluptatem accusantium doloremque laudantium, totam rem aperiam, eaque ipsa quae ab illo inventore veritatis et quasi architecto beatae</p>
    <p>vitae dicta sunt explicabo. Nemo enim ipsam voluptatem quia</p>
  </div>
  <div class="kpi-image" role="img" aria-label="Abstract wave of glowing blue data particles"></div>
</section>

<section class="section partners" id="partners">
  <h2>Trusted Partners</h2>
  <span class="section-rule rule-blue"></span>
  <a class="partner" href="http://www.brevanix.example" style="left:205px"><span class="partner-mark"></span>Brevanix</a>
  <a class="partner" href="http://www.lumicore.example" style="left:475px"><span class="partner-mark"></span>Lumicore</a>
  <a class="partner" href="http://www.dorvale.example.au" style="left:800px"><span class="partner-mark"></span>Dorvale</a>
</section>

<section class="section support" id="support" role="img" aria-label="Dark photo of a hand touching a screen with connection icons">
  <h2>Customer Support</h2>
  <span class="section-rule rule-blue"></span>
  <p>NOC and Customer Support Sed ut perspiciatis unde omnis iste natus error sit voluptatem accusantium doloremque laudantium, totam rem aperiam, eaque ipsa quae ab illo inventore veritatis et quasi architecto beatae vitae dicta sunt explicabo. Nemo enim ipsam voluptatem quia architecto beatae vitae dicta sunt explicabo. Nemo enim ipsam voluptatem quia</p>
  <a class="btn" href="http://www.dorvale.example.au">Get Support</a>
</section>

<section class="section contact" id="contact">
  <h2>Contact Details</h2>
  <span class="section-rule rule-dark"></span>
  <div class="detail" style="left:195px">
    <svg width="44" height="44" viewBox="0 0 44 44" aria-hidden="true"><rect x="8" y="8" width="28" height="28" rx="3" transform="rotate(45 22 22)" fill="var(--red)"/><path d="M29 15 L15 21 L21 23 L23 29 Z" fill="#fff"/></svg>
    <span>72 Alder Row, Unit 14<br>Westbrook, MB R4T 2K8<br>Elsmere</span>
  </div>
  <div class="detail phone" style="left:495px">
    <svg width="44" height="44" viewBox="0 0 44 44" aria-hidden="true"><rect x="8" y="8" width="28" height="28" rx="3" transform="rotate(45 22 22)" fill="var(--red)"/><path d="M16 15 l4 0 l1.5 4 l-2 1.5 a9 9 0 0 0 4.5 4.5 l1.5 -2 l4 1.5 l0 4 a2 2 0 0 1 -2 1 a15 15 0 0 1 -13 -13 a2 2 0 0 1 1.5 -1.5z" fill="#fff"/></svg>
    <span style="margin-top:9px">7810 - 293 - 465</span>
  </div>
  <div class="detail" style="left:755px">
    <svg width="44" height="44" viewBox="0 0 44 44" aria-hidden="true"><rect x="8" y="8" width="28" height="28" rx="3" transform="rotate(45 22 22)" fill="var(--red)"/><rect x="15" y="17" width="14" height="10" fill="#fff"/><path d="M15 17 L22 23 L29 17" stroke="var(--red)" stroke-width="1.5" fill="none"/></svg>
    <span style="margin-top:11px">info@qt482.example</span>
  </div>
  <p class="contact-cta">Contact<br>QT482 today and be in control tomorrow</p>
</section>

<footer class="section site-footer">
  <p class="copyright">Copyright © 2018. All rights reserved.</p>
  <div class="social" aria-label="Social links"><span></span><span></span><span></span></div>
</footer>

</body>
</html>
```